Business card design based on existing website

Please make a business card that is consistent with the look and feel of my new website: http://tellbury.com.sg. By going to the site, I think you'll have all you need in terms of the work I do and the colors I use.

I would like to ask the winner of this project to then do a separate project to design my stationery.

Target Market(s)

Heads of human resources, people wanting psychotherapy, and executives wanting coaching. (It's quite a mix!)

Industry/Entity Type

Psychology

Contact Information for Business Card

Email: ray5678@tellbury.com.sg
Website: http://tellbury.com.sg
Tel: +65 94706218

(I will not have a physical address on the card)

Font styles to use
Serif

Colors

Designer to choose colors to be used in the design.

Requirements
Must have
• On the Front
• ==========
• Have "Dr. Raymond Tellbury" using the font of the website.
• Also "Executive Coach, Psychotherapist, Leadership Professor"
• The back should mention
• ==================
• My degrees
• -------------
• "PhD Kelworth; Post Doc Drayfield". E.g., "Raymond Tellbury (PhD Kelworth; Post Doc Drayfield)" where the text between brackets was in smaller font.
• My work
• ----------
• "Executive coach, psychotherapist, and leadership professor"
• My job titles
• ---------------
• "Principal (Tellbury Consulting)
• Adjunct Professor (Lornvale Commerce University)
• Adjunct Associate Professor (Pemberly Institute of Letters)
• Coach & Supervisor (OKTRAV) '
• Options:
• 1) you can abbreviate Adjunct Professor to "Adj Prof" or "Adj Professor"; and "Adjunct Associate Professor" to "Adj Assoc Prof"
• 2) you abbreviate "Pemberly Institute of Letters" and "Lornvale Commerce University" to "PIL" and "LCU"
• 3) You can also combine the titles for PIL and LCU, e.g., "Adjunct faculty (PIL & LCU)
Nice to have
• Because I work with many Chinese people, it is sometimes helpful to have my family name, "Tellbury", in caps. In the past I have not used caps because it takes away from the aesthetic of the card. Only use caps if it looks good.
• The uploaded image of a "RT" is something that may be helpful. I am undecided.
• THANK YOU for helping me!
Should not have
• No photos. In my industry people consider it overselling.

```html
<!DOCTYPE html>
<html lang="en">
<head>
<meta charset="utf-8">
<title>Dr. Raymond Tellbury – Business Card</title>
<link rel="stylesheet" href="https://fonts.googleapis.com/css2?family=EB+Garamond:wght@500;600&family=Open+Sans:wght@400&display=swap">
<style>
  :root {
    --backdrop: #5c5d5e;
    --forest: #1b3419;
    --cream: #efe8c8;
    --paper-top: #f4f4f4;
    --paper-bottom: #dcdcdc;
    --ink: #222;
    --muted-light: #e8e8e0;
  }
  * { margin: 0; padding: 0; box-sizing: border-box; }
  html, body { width: 1200px; height: 904px; overflow: hidden; }
  body {
    background: var(--backdrop);
    display: flex;
    flex-direction: column;
    align-items: center;
    justify-content: center;
    gap: 44px;
  }
  .card {
    width: 620px;
    height: 354px;
    position: relative;
    overflow: hidden;
    box-shadow: 0 10px 24px rgba(0,0,0,0.35);
  }
  .serif { font-family: "EB Garamond", Garamond, serif; }
  .sans { font-family: "Open Sans", Arial, sans-serif; }

  /* Front */
  .card--front { background: var(--forest); }
  .front-identity { position: absolute; left: 140px; top: 168px; }
  .front-name {
    color: var(--cream);
    font-size: 36px;
    font-weight: 600;
    letter-spacing: 0.5px;
    line-height: 1;
  }
  .front-roles {
    color: var(--muted-light);
    font-size: 13px;
    margin-top: 8px;
    margin-left: 20px;
  }

  /* Back */
  .card--back {
    background: linear-gradient(180deg, var(--paper-top), var(--paper-bottom));
  }
  .back-band {
    position: absolute; left: 0; top: 0; right: 0;
    height: 148px;
    background: var(--forest);
  }
  .back-identity { position: absolute; left: 40px; top: 80px; }
  .back-name {
    color: var(--cream);
    font-size: 36px;
    font-weight: 600;
    letter-spacing: 0.5px;
    line-height: 1;
  }
  .back-degrees {
    color: var(--muted-light);
    font-size: 11px;
    margin-top: 6px;
    margin-left: 20px;
  }
  .titles {
    position: absolute; left: 56px; top: 176px;
    list-style: none;
    color: var(--ink);
    font-size: 14.5px;
    line-height: 20px;
  }
  .contact {
    position: absolute; right: 26px; top: 176px;
    list-style: none;
    color: var(--ink);
    font-size: 14.5px;
    line-height: 20px;
    text-align: right;
  }
  .contact li { display: flex; align-items: center; justify-content: flex-end; gap: 10px; }
  .contact svg { width: 15px; height: 15px; flex: none; }
</style>
</head>
<body>

  <section class="card card--front">
    <div class="front-identity">
      <h1 class="front-name serif">Dr. Raymond Tellbury</h1>
      <p class="front-roles sans">Executive Coach, Psychotherapist, Leadership Trainer</p>
    </div>
  </section>

  <section class="card card--back">
    <div class="back-band"></div>
    <div class="back-identity">
      <h2 class="back-name serif">Dr. Raymond Tellbury</h2>
      <p class="back-degrees sans">(PhD Kelworth; Post Doc Drayfield)</p>
    </div>

    <ul class="titles sans">
      <li>Principal (Tellbury Consulting)</li>
      <li>Adj Prof (LCU)</li>
      <li>Adj Assoc Prof (PIL)</li>
      <li>Coach &amp; Supervisor (OKTRAV)</li>
    </ul>

    <ul class="contact sans">
      <li>+65 94706218
        <svg viewBox="0 0 16 16" aria-hidden="true"><circle cx="8" cy="8" r="8" fill="#1b3419"/><path d="M5.2 4.2l1.6-.4.9 2-1 .8a5 5 0 0 0 2.6 2.6l.8-1 2 .9-.4 1.6c-3.6.3-6.8-2.9-6.5-6.5z" fill="#fff"/></svg>
      </li>
      <li>ray5678@tellbury.com.sg
        <svg viewBox="0 0 16 16" aria-hidden="true"><circle cx="8" cy="8" r="8" fill="#1b3419"/><rect x="4" y="5.2" width="8" height="5.6" fill="#fff"/><path d="M4 5.2l4 3 4-3" fill="none" stroke="#1b3419" stroke-width="0.9"/></svg>
      </li>
      <li>www.tellbury.com.sg
        <svg viewBox="0 0 16 16" aria-hidden="true"><circle cx="8" cy="8" r="8" fill="#1b3419"/><g fill="none" stroke="#fff" stroke-width="0.9"><circle cx="8" cy="8" r="4.2"/><ellipse cx="8" cy="8" rx="1.8" ry="4.2"/><path d="M3.8 8h8.4"/></g></svg>
      </li>
    </ul>
  </section>

</body>
</html>
```